Book cover for "Generous Horizons" encouraging business to take up compassion pr...

I need a book cover designed for "Generous Horizons. Where Winning Falls Short." The book encourages businesses to take up a social mission (that is, to have a social impact, such as corporate social responsibility.) in doing so, they find a greater sense of purpose, their employees and the community are more engaged, and their business grows. I use stories from my podcast Civic Purpose Uprising. 2 key word/phrases that may help t think about are Philanthropy and Corporate Social Responsibility.
This book will be followed by 1 or 2 other books. Another seies of books will also soon requre work.

The market is Mid-sized business owners and CEOs. They have built up the business to a successful place but now find that doesn't bring fulfilment or happiness. The cover needs to have a business or corporate feel.
The Colouring of the book, focus on blues and purples.
This will be a thin book - a quick and easy read of around 110 pages. It is 5x8 inches.
I would be happy to have a photo of me incorporated, but not the focus. I could have a photo done as directed by the designer, as I am planning to have a photoshoot done soon.
Fonts - Please chose a font with the rounded "a", such as in the Century Gothic font, however, open to suggestions.
The back cover will include:
o A book blurb – still to be written
o 2 or 3 endorsements
o Publishing logo (as it is my own publishing company.
o ISBN and barcode
On the spine
• Generous Horizons
• Belinda Morcombe
• Publisher logo icon

For your interest: Belinda is a Speaker, Author, podcaster and Trusted Advisor to Authentic Influencers. Through nourishing community, Belinda maximises the potential of business and influences change.

Target Market(s)

The market is Mid-sized business owners and CEOs. They have built up the business to a successful place but now find that doesn't bring fulfillment or happiness. The cover needs to have a business or corporate feel.

Industry/Entity Type

This is business/corporate book

Font styles to use
Other font styles liked:
• Please chose a font with the rounded "a", such as in the Century Gothic font, however, open to suggestions.

Colors
0054AA
0677BA
7BADD7
CADEEF
E8F1F8
A7469A
B969AE
D3A5CF
EDDBEB
F8F0F9
6B429C
8869AF
B7A5CE
E3DAEB
F3F0F8

Requirements
Must have
• An eye catching design with a business feel.
Nice to have
• I would be nice to edit me into the cover somehow - like Lindqvist puts himself in the background of his movies. I can have photos taken to match .

```html
<!DOCTYPE html>
<html lang="en">
<head>
<meta charset="utf-8">
<title>Generous Horizons – Book Cover</title>
<link rel="stylesheet" href="https://fonts.googleapis.com/css2?family=Montserrat:wght@700;800&family=Questrial&display=swap">
<style>
  :root {
    --page-bg: #e9eaec;
    --cover-bg: #ffffff;
    --title-blue: #0054aa;
    --accent-blue: #0677ba;
    --light-blue: #7badd7;
    --magenta: #a7469a;
    --magenta-deep: #a3207c;
  }
  * { margin: 0; padding: 0; box-sizing: border-box; }
  html, body {
    width: 1200px;
    height: 1200px;
    overflow: hidden;
    background: var(--page-bg);
  }
  .canvas {
    position: relative;
    width: 1200px;
    height: 1200px;
  }
  .cover {
    position: absolute;
    left: 275px;
    top: 100px;
    width: 650px;
    height: 1000px;
    background: var(--cover-bg);
    box-shadow: 0 6px 24px rgba(0,0,0,0.12);
    overflow: hidden;
  }
  .tagline {
    position: absolute;
    top: 62px;
    left: 0;
    width: 100%;
    text-align: center;
    font-family: "Questrial", "Century Gothic", sans-serif;
    font-size: 33px;
    color: var(--title-blue);
    letter-spacing: -0.01em;
  }
  .tagline em {
    font-family: "Montserrat", sans-serif;
    font-weight: 700;
    font-style: italic;
    letter-spacing: -0.02em;
  }
  .title {
    position: absolute;
    top: 258px;
    left: 0;
    width: 100%;
    text-align: center;
    color: var(--title-blue);
  }
  .title-main {
    display: block;
    font-family: "Montserrat", sans-serif;
    font-weight: 800;
    font-size: 128px;
    line-height: 124px;
    letter-spacing: 0.01em;
  }
  .title-sub {
    display: block;
    margin-top: 6px;
    font-family: "Questrial", "Century Gothic", sans-serif;
    font-size: 94px;
    line-height: 100px;
    color: var(--magenta-deep);
    letter-spacing: -0.01em;
  }
  .feature-art {
    position: absolute;
    left: 50px;
    top: 585px;
    width: 526px;
    height: 80px;
    border-radius: 0 0 50% 50% / 0 0 100% 100%;
    background: linear-gradient(180deg, var(--accent-blue), var(--title-blue));
  }
  .author {
    position: absolute;
    top: 795px;
    left: 0;
    width: 100%;
    text-align: center;
    font-family: "Montserrat", sans-serif;
    font-weight: 700;
    font-size: 42px;
    line-height: 78px;
    color: var(--magenta-deep);
    letter-spacing: 0.95em;
    text-indent: 0.95em;
  }
  .author span { display: block; }
</style>
</head>
<body>
  <main class="canvas">
    <section class="cover" aria-label="Book cover: Generous Horizons by Belinda Morcombe">
      <p class="tagline">Where <em>Winning</em> Falls <em>Short</em></p>
      <h1 class="title">
        <span class="title-main">GENER</span>
        <span class="title-main">OUS</span>
        <span class="title-sub">HORIZONS</span>
      </h1>
      <div class="feature-art" role="img" aria-label="Curved blue feather lying beneath the title"></div>
      <p class="author">
        <span>BELINDA</span>
        <span>MORCOMBE</span>
      </p>
    </section>
  </main>
</body>
</html>
```